Turm7Zwerge
Zielgruppe
Zielgruppe sind die Eltern, Lehrer, Kindergärtner, aber auch Kinder, die bereits Lesen können.
Aufgabenstellung
Ich brauche einen Flyer und ein Plakat für eine Kinderschachschule für Kinder zwischen 4 und 15 Jahren. Auf dem Flyer, den ich in A6-Format drucken möchte (beidseitig), muss ich die Info über die Kinderschachschule Turm7Zwerge (mehr Infos unter www.turm7zwerge-beispiel.ch), dh., was wir machen, Kontaktdaten, etc schreiben können. Es dient als Werbematerial zum Auslegen
Auf dem Plakat wird mehr oder weniger das Gleiche stehen, es wird jedoch als Din A4 Seite aufgehängt.
Unsere Kontaktinformation ist wie folgt:
Turm7Zwerge: Spielen mit kleinen Strategen
www.turm7zwerge-beispiel.ch

```html
<!DOCTYPE html>
<html lang="de">
<head>
<meta charset="utf-8">
<title>Turm7Zwerge – Kinderschach</title>
<link href="https://fonts.googleapis.com/css2?family=Arimo:ital,wght@0,400;0,700;1,700&family=Chewy&display=swap" rel="stylesheet">
<style>
  :root {
    --gold-band: #c8902b;
    --band-text: #f6ecd6;
    --heading-blue: #1b8fd8;
    --frame-blue: #2a8fd0;
    --claim-orange: #f2a21c;
    --claim-edge: #9a5a08;
    --accent-pink: #d51a7c;
    --text-dark: #2b2b2b;
    --paper: #ffffff;
    --check-light: #f3f3f3;
    --check-dark: #e2e2e2;
  }
  * { margin: 0; padding: 0; box-sizing: border-box; }
  html, body { width: 851px; height: 1200px; overflow: hidden; background: var(--paper); }
  .poster {
    position: relative;
    width: 851px; height: 1200px;
    background: var(--paper);
    font-family: "Arimo", Arial, sans-serif;
    color: var(--text-dark);
    overflow: hidden;
  }
  .board-backdrop {
    position: absolute; left: 147px; top: 360px; right: 0; bottom: 0;
    background: linear-gradient(160deg, var(--paper) 0%, var(--check-light) 35%, var(--check-dark) 100%);
  }
  .side-band {
    position: absolute; left: 0; top: 0; width: 147px; height: 1200px;
    background: var(--gold-band);
  }
  .side-band__url {
    position: absolute; left: 100px; top: 1160px;
    transform: rotate(-90deg); transform-origin: left top;
    white-space: nowrap;
    font-weight: 700; font-size: 25px; letter-spacing: 0.5px;
    color: var(--band-text);
  }
  .brand {
    position: absolute; left: 500px; top: 70px; width: 320px;
    text-align: center;
  }
  .brand__name {
    display: inline-flex; align-items: center; gap: 12px;
    font-weight: 700; font-size: 46px; color: var(--accent-pink);
  }
  .brand__mark { width: 22px; height: 22px; background: var(--accent-pink); }
  .brand__tagline {
    margin-top: 6px; font-weight: 700; font-size: 17px;
    letter-spacing: 0.5px; text-transform: uppercase; color: var(--text-dark);
  }
  .headline {
    position: absolute; left: 175px; top: 222px;
    font-weight: 700; font-style: italic; font-size: 32px; line-height: 36px;
    color: var(--heading-blue);
    text-shadow: 1px 2px 2px rgba(0,0,0,0.25);
  }
  .photo {
    position: absolute; background: var(--paper);
    border: 3px solid var(--frame-blue); padding: 8px;
    box-shadow: 2px 3px 6px rgba(0,0,0,0.3);
  }
  .photo__fill { width: 100%; height: 100%; }
  .photo--lesson { left: 52px; top: 382px; width: 355px; height: 258px; transform: rotate(-4deg); }
  .photo--lesson .photo__fill { background: linear-gradient(135deg, #3b2c22, #7d6550 55%, #c9b9a3); }
  .photo--match { left: 468px; top: 848px; width: 332px; height: 212px; transform: rotate(3deg); }
  .photo--match .photo__fill { background: linear-gradient(135deg, #2e241d, #6f5a47 55%, #c4b39c); }
  .claims {
    position: absolute; left: 452px; top: 425px; list-style: none;
  }
  .claims li {
    display: flex; align-items: center; gap: 10px;
    height: 55px;
    font-family: "Chewy", cursive; font-size: 33px; letter-spacing: 0.5px;
    color: var(--claim-orange);
    text-shadow: 1px 1px 0 var(--claim-edge), -1px 1px 0 var(--claim-edge), 1px -1px 0 var(--claim-edge), -1px -1px 0 var(--claim-edge), 2px 3px 3px rgba(0,0,0,0.3);
  }
  .diamond { width: 14px; height: 14px; transform: rotate(45deg); flex: none; }
  .claims .diamond { background: var(--accent-pink); width: 15px; height: 15px; }
  .intro {
    position: absolute; left: 175px; top: 696px; width: 640px;
    font-size: 19px; line-height: 30px;
  }
  .training {
    position: absolute; left: 167px; top: 774px; list-style: none;
    font-size: 19px;
  }
  .training li { display: flex; align-items: center; gap: 14px; height: 32px; }
  .training .diamond { background: var(--frame-blue); width: 10px; height: 10px; }
  .contact {
    position: absolute; left: 175px; top: 1068px;
    font-size: 19px; line-height: 29px;
  }
  .contact__name { color: var(--accent-pink); margin-bottom: 2px; }
  .contact__row { display: flex; }
  .contact__row span:first-child { width: 205px; }
</style>
</head>
<body>
<main class="poster">
  <div class="board-backdrop"></div>

  <aside class="side-band">
    <div class="side-band__url">www.turm7zwerge-beispiel.ch</div>
  </aside>

  <header class="brand">
    <div class="brand__name"><span class="brand__mark"></span>Turm7Zwerge</div>
    <div class="brand__tagline">Spielen mit kleinen Strategen</div>
  </header>

  <h1 class="headline">Kinderschach:<br>Wir bringen Ihr Kind<br>Zug um Zug zum Erfolg!</h1>

  <figure class="photo photo--lesson">
    <div class="photo__fill" role="img" aria-label="Foto: zwei Kinder spielen Schach an einem Brett"></div>
  </figure>

  <ul class="claims">
    <li><span class="diamond"></span>Schach macht Spaß!</li>
    <li><span class="diamond"></span>Schach macht stark!</li>
    <li><span class="diamond"></span>Schach macht schlau!</li>
    <li><span class="diamond"></span>Schach statt Tabletten!</li>
  </ul>

  <p class="intro">Wir bieten täglich hochwertige kindgerechte Schachkurse für Kinder ab 4 Jahren an. Unser Schachtraining beinhaltet:</p>

  <ul class="training">
    <li><span class="diamond"></span>Konzentrationstraining</li>
    <li><span class="diamond"></span>Vertrauensaufbau</li>
    <li><span class="diamond"></span>Stärkung des Selbstvertrauens</li>
    <li><span class="diamond"></span>Persönliches Wachstum</li>
    <li><span class="diamond"></span>Geistige Herausforderung</li>
    <li><span class="diamond"></span>Intelektuelle Stärkung</li>
  </ul>

  <figure class="photo photo--match">
    <div class="photo__fill" role="img" aria-label="Foto: Kinder beim Schachspiel im Kurs"></div>
  </figure>

  <address class="contact" style="font-style: normal;">
    <div class="contact__name">Turm7Zwerge</div>
    <div class="contact__row"><span>Lärchenweg 12</span><span>Tel.: 079-000 12 34</span></div>
    <div class="contact__row"><span>8999 Seedorf</span><span>info@turm7zwerge-beispiel.ch</span></div>
  </address>
</main>
</body>
</html>
```